Consulting company (stride-and-calm, previously stundenwerk lübeck) needs design for a clear and fre

This website is to be made completely new with Worpreess / Divi. I am at the beginning and have no idea about the design. The design is the focus of this order. After the first website I would like to use the design and colors for all other design products for business, which will be placed here as well.
On the website the services, the team, references ... should be separate pages. Please see the attached document. A very important part is the blog and the categories should be visible in the desktop view, vie widgets.

The site should be clear, well-arranged, but still convey freshness and vitality.
Our company offers consulting and online trainings for the following topics:
- Digital paperless office
- process optimization, digitalization
- Remote working and productivity
- Remote leadership
- remote project management
- Time management 4. 0
- Focus on the essentials

We do this in the form of:
- Keynote Speaking
- Facilitating
- Presentation
- Workshops and trainings
- Online trainings

Our services are intended exclusively for companies.

What drives us?
We want to inspire our customers to work more green, lean digital and focus on the essentials. We are a team of three people who are digital nomads, but who also work offline on site.
I do have already webseites, but they are old, but give you an idea what we do: stundenwerk-luebeck.example. and ms-inkfree.example.

One style of a web site I like is for example is that of "plenvoro.example" Colors I thought so far, but I'm not sure, could be the color palette "vandal pigment" from drafbel.example or something similar to # f60b80a and # 39dfa7. But I am open for other suggestions.
I love simple and clear fonts. I like this contemporary style of sites, where you get most of the content on the mobile devices by scrolling.

Target Market(s)

midsize and large businesses, decision maker

Logo Text

Let's work calm and focused

Number of Pages Required

5+ page

Font styles to use
Sans Serif

Colors
e34297
00a990

Requirements
Must have
• the page should be clear and concise, much white with color accents like content blocks or headlines, responsive,
Nice to have
• I like interesting backgrounds, very discreet, perhaps white and gray or the color shades of pastel, the site should somehow fit to the photos, the logo I added is the old one, just to give you an idea
Should not have
• in no case too playful or loud

```html
<!DOCTYPE html>
<html lang="en">
<head>
<meta charset="utf-8">
<title>Stride and Calm – Digital Change Agent</title>
<link rel="stylesheet" href="https://fonts.googleapis.com/css2?family=Roboto:wght@400;500;700&family=Lato:wght@400;700&display=swap">
<style>
:root{
  --pink:#e5147f;
  --green:#2fcf8c;
  --mint:#e6f7f2;
  --ink:#111;
  --white:#fff;
}
*{box-sizing:border-box;margin:0;padding:0}
html,body{width:1200px;height:3418px;overflow:hidden}
body{position:relative;font-family:"Roboto",Arial,sans-serif;color:var(--ink);background:var(--white)}
.abs{position:absolute}

.topbar{left:0;top:0;width:1200px;height:49px;background:var(--mint)}
.social-dot{width:30px;height:30px;border:2px solid var(--pink);border-radius:50%;top:10px}
.contact-line{top:16px;font-size:15px;color:#222;white-space:nowrap}
.contact-line svg{vertical-align:-3px;margin-right:5px}

.header{left:0;top:49px;width:1200px;height:102px;background:var(--white)}
.brand{left:82px;top:72px;display:flex;align-items:center;gap:10px}
.brand-mark{width:46px;height:46px;border-radius:50%;background:var(--green)}
.brand-name{font-size:25px;font-weight:700;color:var(--green);line-height:1.1}
.brand-tag{font-size:12px;font-weight:700;color:var(--green);letter-spacing:.3px}
.nav{top:94px;font-size:17px;font-weight:500;color:#222}
.nav.active{color:var(--pink)}
.nav-underline{left:472px;top:145px;width:65px;height:4px;background:var(--pink)}

.hero{left:0;top:151px;width:1200px;height:576px;overflow:hidden;
  background:linear-gradient(90deg,#3f9e8c 0%,#6a8f8f 35%,#b5568f 70%,#e2157f 100%)}
.hero-title{left:133px;top:314px;font-size:42px;font-weight:700;color:var(--white);line-height:1.05}
.hero-text{left:136px;top:420px;font-size:19px;color:var(--white);line-height:27px;width:460px}
.btn-ghost{left:134px;top:499px;width:196px;height:52px;border:3px solid var(--white);border-radius:30px;color:var(--white);font-size:17px;font-weight:500;display:flex;align-items:center;justify-content:center;letter-spacing:.5px}
.hero-dot{left:1122px;width:13px;height:13px;border-radius:50%;background:var(--white)}
.hero-dot.ring{background:transparent;border:2px solid var(--white)}

.about-img{left:127px;top:836px;width:473px;height:315px;border-radius:6px;background:linear-gradient(135deg,#6b7a80,#c9c4be 55%,#2d6b4f)}
.eyebrow{left:653px;top:840px;font-size:23px;color:var(--green)}
.about-title{left:652px;top:870px;font-size:35px;font-weight:700}
.about-text{left:652px;top:933px;width:440px;font-size:15.5px;line-height:27px;color:#444}
.about-text p+p{margin-top:14px}
.btn-pink{left:652px;top:1103px;width:180px;height:47px;border:2px solid var(--pink);border-radius:30px;color:var(--pink);font-size:16px;font-weight:500;display:flex;align-items:center;justify-content:center}

.services{left:0;top:1233px;width:1200px;height:604px;background:var(--mint)}
.section-title{font-size:30px;font-weight:700;text-align:center;width:1200px;left:0}
.hub-name{left:479px;top:1470px;width:234px;text-align:center;font-size:26px;font-weight:700;color:var(--green)}
.svc-name{font-size:17px;font-weight:700;color:var(--pink)}
.svc-text{font-size:12.5px;color:#555;line-height:17px;font-family:"Lato",Arial,sans-serif}
.right{text-align:right}

.testimonials{left:0;top:1837px;width:1200px;height:501px;background:linear-gradient(90deg,#2c8f86 0%,#5f6f8f 45%,#8a4f8d 75%,#b0488f 100%)}
.card{top:1965px;width:296px;height:283px;background:var(--white);border-radius:3px;text-align:center;padding-top:27px}
.card.dark{background:rgba(70,60,100,.55)}
.avatar{width:72px;height:72px;border-radius:50%;margin:0 auto;background:linear-gradient(135deg,#8fa3b4,#4d5d6b)}
.card-name{margin-top:8px;font-size:18px;font-weight:700;color:#3a9c86}
.card-city{font-size:15px;font-weight:500;color:#3a9c86}
.card.dark .card-name,.card.dark .card-city,.card.dark .card-text{color:var(--white)}
.card-text{margin:18px auto 0;width:240px;font-size:13.5px;line-height:22px;color:#888}

.blog-title{left:135px;top:2402px;font-size:33px;font-weight:700}
.blog-img{background:linear-gradient(135deg,#b8bdc3,#d8dadd 50%,#8c5a70)}
.meta{font-family:"Lato",Arial,sans-serif;font-size:14px;font-weight:700;color:var(--pink)}
.post-title{font-family:"Lato",Arial,sans-serif;font-size:19px;color:#222;line-height:25px;text-transform:uppercase}
.post-text{font-family:"Lato",Arial,sans-serif;font-size:13.5px;color:#555;line-height:22px}
.more{font-family:"Lato",Arial,sans-serif;font-size:17px;font-weight:700;color:#1fa77a}
.divider{left:622px;width:437px;height:1px;background:#ccc}

.footer{left:0;top:3010px;width:1200px;height:408px}
.f-head{font-size:19px;font-weight:700;color:var(--white)}
.f-list{font-size:14px;color:var(--white);line-height:23px}
.f-small{font-size:10px;color:var(--white)}
.f-social{width:36px;height:36px;border:2px solid var(--white);border-radius:50%}
</style>
</head>
<body>

<div class="abs topbar"></div>
<div class="abs social-dot" style="left:96px"></div>
<div class="abs social-dot" style="left:134px"></div>
<div class="abs social-dot" style="left:172px"></div>
<div class="abs contact-line" style="left:640px">
  <svg width="16" height="16" viewBox="0 0 24 24" fill="#e5147f"><path d="M6.6 10.8a15 15 0 0 0 6.6 6.6l2.2-2.2c.3-.3.7-.4 1-.2 1.1.4 2.3.6 3.6.6.6 0 1 .4 1 1V20c0 .6-.4 1-1 1A17 17 0 0 1 3 4c0-.6.4-1 1-1h3.5c.6 0 1 .4 1 1 0 1.3.2 2.5.6 3.6.1.3 0 .7-.2 1z"/></svg>Phone: +49 170 5550 12 34</div>
<div class="abs contact-line" style="left:882px">
  <svg width="16" height="14" viewBox="0 0 24 18" fill="#e5147f"><path d="M0 0h24v18H0z M2 2l10 7 10-7" stroke="#fff" stroke-width="1.5"/></svg>info@stundenwerk-luebeck.example</div>

<div class="abs header"></div>
<div class="abs brand">
  <div class="brand-mark"></div>
  <div>
    <div class="brand-name">Stride and Calm</div>
    <div class="brand-tag">LET'S WORK CALM AND FOCUSED</div>
  </div>
</div>
<div class="abs nav active" style="left:479px">Home</div>
<div class="abs nav" style="left:572px">Sample Page</div>
<div class="abs nav" style="left:721px">About Us</div>
<div class="abs nav" style="left:840px">Services</div>
<div class="abs nav" style="left:955px">Blog</div>
<div class="abs nav" style="left:1038px">Contact Us</div>
<div class="abs nav-underline"></div>

<section class="abs hero" role="img" aria-label="Photo of a smiling consultant in a checked blazer working at a laptop"></section>
<h1 class="abs hero-title">Digital Change Agent &amp;<br>Efficiency Trainer</h1>
<p class="abs hero-text">Lorem ipsum dolor sit amet consectetuer adipiscing elit Nam cursus Morbi ut mi Nullam ea</p>
<div class="abs btn-ghost">LEARN MORE</div>
<div class="abs hero-dot ring" style="top:375px"></div>
<div class="abs hero-dot" style="top:398px"></div>
<div class="abs hero-dot" style="top:420px"></div>
<div class="abs hero-dot" style="top:442px"></div>

<div class="abs about-img" role="img" aria-label="Photo of the consultant in a green blazer at a laptop in an office"></div>
<div class="abs eyebrow">Who We Are</div>
<h2 class="abs about-title">About Stride and Calm</h2>
<div class="abs about-text">
  <p>Augiat in pede Fusce tellus Sed metus augue convallis et vehicula ut pulvinar eu ante Integer orci tellus</p>
  <p>Atristique vitae consequat nec mauris viverra in gravida eu mattis in ante Morbi eget arcurmentum vel congue &nbsp;elit Fusce ultricies orci ac feugiat suscipit leo massa sodales velit</p>
</div>
<div class="abs btn-pink">LEARN MORE</div>

<section class="abs services"></section>
<h2 class="abs section-title" style="top:1287px">What We Do</h2>
<svg class="abs" style="left:0;top:0" width="1200" height="1800" viewBox="0 0 1200 1800">
  <path d="M488 1400 A138 138 0 1 0 721 1542" fill="none" stroke="#2fcf8c" stroke-width="2"/>
  <g fill="#fff" stroke="#2fcf8c" stroke-width="2">
    <circle cx="488" cy="1401" r="7"/><circle cx="704" cy="1401" r="7"/>
    <circle cx="721" cy="1542" r="7"/><circle cx="596" cy="1624" r="7"/>
  </g>
  <circle cx="596" cy="1486" r="117" fill="#fff"/>
  <g fill="#fff" stroke="#e0e0e0" stroke-width="1">
    <circle cx="410" cy="1415" r="34"/><circle cx="791" cy="1417" r="34"/>
    <circle cx="422" cy="1561" r="34"/><circle cx="775" cy="1568" r="34"/>
    <circle cx="597" cy="1680" r="34"/>
  </g>
  <g fill="none" stroke="#e5147f" stroke-width="2">
    <path d="M398 1428l20-20M404 1405l10 10"/>
    <circle cx="791" cy="1413" r="9"/><path d="M787 1424h8v6h-8z"/>
    <rect x="407" y="1547" width="30" height="20"/><path d="M416 1573h12"/>
    <rect x="769" y="1552" width="12" height="8"/><path d="M775 1560v8M761 1568h28M761 1568v6M775 1568v6M789 1568v6"/>
    <rect x="583" y="1666" width="28" height="22"/><circle cx="597" cy="1677" r="5"/>
  </g>
</svg>
<div class="abs hub-name">Stride and Calm</div>
<div class="abs right" style="left:150px;top:1384px;width:208px">
  <div class="svc-name">Keynote Speaking</div>
  <div class="svc-text">Aurmentum vel congue &nbsp;elit Fusce<br>ultricies orci ac feugiat suscipit</div>
</div>
<div class="abs" style="left:841px;top:1388px">
  <div class="svc-name">Facilitating</div>
  <div class="svc-text">Aurmentum vel congue &nbsp;elit Fusce<br>ultricies orci ac feugiat suscipit</div>
</div>
<div class="abs right" style="left:150px;top:1538px;width:226px">
  <div class="svc-name">Workshops and trainings</div>
  <div class="svc-text">Aurmentum vel congue &nbsp;elit Fusce<br>ultricies orci ac feugiat suscipit</div>
</div>
<div class="abs" style="left:826px;top:1535px">
  <div class="svc-name">Presentation</div>
  <div class="svc-text">Aurmentum vel congue &nbsp;elit Fusce<br>ultricies orci ac feugiat suscipit</div>
</div>
<div class="abs" style="left:400px;top:1726px;width:400px;text-align:center">
  <div class="svc-name">Online Trainings</div>
  <div class="svc-text">Aurmentum vel congue &nbsp;elit Fusce<br>ultricies orci ac feugiat suscipit</div>
</div>

<section class="abs testimonials" role="img" aria-label="Faded background photo of a consultant, tinted teal to pink"></section>
<h2 class="abs section-title" style="top:1888px;color:#fff">Testimonials</h2>
<div class="abs card" style="left:138px">
  <div class="avatar" role="img" aria-label="Client portrait"></div>
  <div class="card-name">Author Name</div><div class="card-city">City Location</div>
  <p class="card-text">Alit Fusce ultricies orci ac feugiat suscipit leo massa sodales velit et scelerisque quam Curabitur vel dolor ultrices ipsum dictum tristique</p>
</div>
<div class="abs card dark" style="left:463px">
  <div class="avatar" role="img" aria-label="Client portrait"></div>
  <div class="card-name">Author Name</div><div class="card-city">City Location</div>
  <p class="card-text">Alit Fusce ultricies orci ac feugiat suscipit leo massa sodales velit et scelerisque quam Curabitur vel dolor ultrices ipsum dictum tristique</p>
</div>
<div class="abs card" style="left:788px">
  <div class="avatar" role="img" aria-label="Client portrait"></div>
  <div class="card-name">Author Name</div><div class="card-city">City Location</div>
  <p class="card-text">Alit Fusce ultricies orci ac feugiat suscipit leo massa sodales velit et scelerisque quam Curabitur vel dolor ultrices ipsum dictum tristique</p>
</div>
<svg class="abs" style="left:98px;top:2076px" width="22" height="36" viewBox="0 0 22 36"><path d="M18 3L4 18l14 15" fill="none" stroke="#fff" stroke-width="4"/></svg>
<svg class="abs" style="left:1100px;top:2076px" width="22" height="36" viewBox="0 0 22 36"><path d="M4 3l14 15L4 33" fill="none" stroke="#fff" stroke-width="4"/></svg>

<h2 class="abs blog-title">Latest Blogs</h2>
<div class="abs blog-img" style="left:133px;top:2466px;width:448px;height:253px" role="img" aria-label="Photo of the consultant in a dark blazer by an office window"></div>
<div class="abs" style="left:144px;top:2750px;width:420px">
  <div class="meta">April 12, 2019 &nbsp;| &nbsp;No Comments</div>
  <div class="post-title" style="margin-top:10px">Mauris vel lacus vitae felis vestibulum volutpat etiam est nunc</div>
  <p class="post-text" style="margin-top:12px">Nunc tempus felis vitae urna Vivamus porttitor neque at volutpat rutrum purus nisi eleifend libero a tempus libero lectus</p>
  <div class="more" style="margin-top:12px">Learn More</div>
</div>

<div class="abs blog-img" style="left:622px;top:2466px;width:147px;height:125px" role="img" aria-label="Photo of a woman with a headset at a laptop"></div>
<div class="abs" style="left:788px;top:2474px;width:280px">
  <div class="meta">April 08, 2019 &nbsp;| &nbsp;No Comments</div>
  <div class="post-title" style="margin-top:6px">Mauris vel lacus vitae felis vestibulum volutpat</div>
  <div class="more" style="margin-top:10px">Learn More</div>
</div>
<div class="abs divider" style="top:2609px"></div>

<div class="abs blog-img" style="left:623px;top:2634px;width:147px;height:125px" role="img" aria-label="Photo of a speaker with a microphone in front of an audience"></div>
<div class="abs" style="left:790px;top:2630px;width:280px">
  <div class="meta">April 06, 2019 &nbsp;| &nbsp;No Comments</div>
  <div class="post-title" style="margin-top:6px">Fusce tellus sed metus augue convallis et</div>
  <div class="more" style="margin-top:10px">Learn More</div>
</div>
<div class="abs divider" style="top:2779px"></div>

<div class="abs blog-img" style="left:624px;top:2801px;width:147px;height:125px" role="img" aria-label="Photo of a trainer presenting to a seated group"></div>
<div class="abs" style="left:792px;top:2802px;width:280px">
  <div class="meta">April 02, 2019 &nbsp;| &nbsp;No Comments</div>
  <div class="post-title" style="margin-top:6px">Phasellus felis dolor scelerisque a tempus</div>
  <div class="more" style="margin-top:10px">Learn More</div>
</div>

<svg class="abs footer" viewBox="0 0 1200 408" preserveAspectRatio="none">
  <path d="M0 45 C300 -5 550 40 800 20 C950 8 1100 5 1200 10 L1200 408 L0 408 Z" fill="#34d98e"/>
  <line x1="115" y1="346" x2="1080" y2="346" stroke="#ffffff" stroke-opacity=".5"/>
</svg>
<div class="abs" style="left:108px;top:3140px;width:240px;text-align:center">
  <div style="width:50px;height:50px;border-radius:50%;border:2px solid #fff;margin:0 auto 14px"></div>
  <div style="font-size:25px;font-weight:700;color:#fff">Stride and Calm</div>
  <div style="font-size:12px;font-weight:700;color:#fff;margin-top:4px">LET'S WORK CALM AND FOCUSED</div>
</div>
<div class="abs" style="left:386px;top:3130px">
  <div class="f-head">Quick Links</div>
  <div class="f-list" style="margin-top:10px">About Us<br>Our Services<br>Why Us<br>Contact Us</div>
</div>
<div class="abs" style="left:557px;top:3127px">
  <div class="f-head">Resources</div>
  <div class="f-list" style="margin-top:10px">Blogs<br>Testimonial<br>Support<br>News</div>
</div>
<div class="abs" style="left:704px;top:3131px;width:190px">
  <div class="f-head">Contact Us</div>
  <div class="f-list" style="margin-top:10px;font-size:13px">(555) 014 2252<br>info@stride-and-calm.example</div>
  <div style="display:flex;gap:5px;margin-top:14px">
    <div class="f-social"></div><div class="f-social"></div><div class="f-social"></div>
  </div>
</div>
<div class="abs" style="left:906px;top:3127px;width:215px">
  <div class="f-head">Latest Tweets</div>
  <div class="f-list" style="margin-top:10px;font-size:13px;line-height:19px">Augiat in pede Fusce tellus Sed metus augue convallis</div>
  <div class="f-small" style="margin-top:3px">Posted 2 days ago</div>
  <div class="f-list" style="margin-top:20px;font-size:13px;line-height:19px">Curabitur vel dolor ultrices ipsum dictum tristique Praesent</div>
  <div class="f-small" style="margin-top:3px">Posted 2 days ago</div>
</div>
<div class="abs" style="left:0;top:3376px;width:1200px;text-align:center;font-size:13px;color:#fff">© 2020 Company Name | All Rights Reserved | Disclaimer</div>

</body>
</html>
```